Create Brisk Lesson Studio a card design that will stick in the mind of prospects.

Brisk Lesson Studio specialises designs and produces training video, animation, illustration and text.

We need a card design that oozes class and leaves the prospect brimming with confidence.

The design will feature the Brisk Lesson Studio all black logo (uploaded). The design may also use the shade of orange from the orange version of the logo (uploaded). Note, just the color is to be used e.g. for the back of the card, not the orange logo itself.

The Brisk brand is about authenticity, quality, maturity and assurance. We are a safe buy when it comes to the prospects next project.

Target Market(s)

The primary target is training managers or others who are responsible for choosing to hire companies to produce their training media e.g. video. This will usually be a large spend so they need to have confidence.

Industry/Entity Type

Training

Contact Information for Business Card

FRONT:

Brisk Lesson Studio
Phone: 03 5172 4039
1st Floor, 418 Kellerby Road
Mt Ferncombe
VIC 3862
Australia
www.brisklesson.com.au

Lionel Petch
Founder and Lead Consultant
mobile: +61 3 0462 735 218
email: lionel@brisklesson.com.au

BACK:
Specialising in design and production of training:

video
animation
illustration
text

for delivery via internet, intranet and/or LMS.

Number of Pages Required

4 page

Font styles to use
Sans Serif

Requirements
Must have
• The black logo uploaded with the brief.
Nice to have
• The inclusion of the shade of orange found in the orange logo also uploaded with the brief. One example would be having the back of the card in this orange and using a white font for the text. But I want the designer to work this out.
Should not have
• No colours other than black and the orange included in the uploaded orange logo.

```html
<!DOCTYPE html>
<html lang="en">
<head>
<meta charset="utf-8">
<title>Brisk Lesson Studio – Business Card Front and Back</title>
<link rel="stylesheet" href="https://fonts.googleapis.com/css2?family=Montserrat:wght@400;500;600&display=swap">
<style>
  :root {
    --backdrop: #3b3b3b;
    --card: #ffffff;
    --ink: #1a1a1a;
    --orange: #f26522;
    --muted: #9a9a9a;
    --panel-light: #d9d9d9;
    --panel-dark: #8c8c8c;
  }
  * { box-sizing: border-box; margin: 0; padding: 0; }
  html, body { width: 1200px; height: 723px; overflow: hidden; }
  body {
    background: var(--backdrop);
    font-family: "Montserrat", sans-serif;
    color: var(--ink);
    position: relative;
  }
  .sheet-title {
    position: absolute;
    left: 45px;
    top: 140px;
    color: #ffffff;
    font-weight: 400;
    font-size: 30px;
    letter-spacing: 0.5px;
  }
  .card {
    position: absolute;
    top: 200px;
    width: 540px;
    height: 316px;
    background: var(--card);
    overflow: hidden;
  }
  .card--front { left: 45px; }
  .card--back { left: 615px; }

  .stripe-panel {
    position: absolute;
    top: 0;
    height: 100%;
    background: linear-gradient(135deg, var(--panel-light), var(--panel-dark) 55%, var(--panel-light));
  }
  .card--front .stripe-panel { left: 395px; width: 145px; }
  .card--back .stripe-panel { left: 0; width: 253px; }

  .brand-mark {
    position: absolute;
    top: 132px;
    transform: translate(-50%, -50%);
    font-weight: 600;
    font-size: 50px;
    color: var(--ink);
    line-height: 1;
  }
  .card--front .brand-mark { left: 435px; }
  .card--back .brand-mark { left: 155px; }

  .contact {
    position: absolute;
    left: 52px;
    font-size: 14px;
    line-height: 19px;
  }
  .contact--company { top: 46px; }
  .contact--person { top: 200px; }
  .contact__name {
    color: var(--orange);
    font-weight: 500;
    font-size: 16px;
  }
  .contact__line { display: flex; align-items: center; gap: 7px; }
  .contact__line--indent { padding-left: 0; }
  .icon { width: 12px; height: 12px; flex: none; }

  .services {
    position: absolute;
    left: 323px;
    top: 42px;
    font-size: 14px;
    line-height: 19px;
    font-weight: 500;
    text-transform: uppercase;
  }
  .services__list { list-style: none; margin: 16px 0 20px; }
  .services__list li { display: flex; align-items: center; gap: 8px; }
  .services__delivery { text-transform: none; font-weight: 500; }

  .web-address {
    position: absolute;
    left: 527px;
    top: 158px;
    transform: translate(-50%, -50%) rotate(90deg);
    font-size: 13px;
    letter-spacing: 2.5px;
    color: var(--muted);
    white-space: nowrap;
  }
</style>
</head>
<body>
  <h1 class="sheet-title">BUSINESS CARD FRONT AND BACK</h1>

  <section class="card card--front" aria-label="Card front">
    <div class="stripe-panel" role="img" aria-label="Diagonal black and orange stripe pattern"></div>
    <div class="brand-mark">Brisk</div>

    <div class="contact contact--company">
      <p class="contact__name">Brisk Lesson Studio</p>
      <p class="contact__line">
        <svg class="icon" viewBox="0 0 12 12"><path d="M2 1h3l1 3-1.5 1a6 6 0 0 0 2.5 2.5L8 6l3 1v3a1 1 0 0 1-1 1A9 9 0 0 1 1 2a1 1 0 0 1 1-1z" fill="var(--orange)"/></svg>
        03 5172 4039
      </p>
      <p>1st Floor, 418 Kellerby Road</p>
      <p>Mt Ferncombe</p>
      <p>VIC 3862</p>
      <p>Australia</p>
      <p class="contact__line">
        <svg class="icon" viewBox="0 0 12 12"><circle cx="6" cy="6" r="5.5" fill="var(--orange)"/><path d="M0.5 6h11M6 0.5v11" stroke="#fff" stroke-width="0.9"/></svg>
        brisklesson.com.au
      </p>
    </div>

    <div class="contact contact--person">
      <p class="contact__name">Lionel Petch</p>
      <p>Founder and Lead Consultant</p>
      <p class="contact__line">
        <svg class="icon" viewBox="0 0 12 12"><rect x="3" y="0.5" width="6" height="11" rx="1" fill="var(--orange)"/><rect x="4" y="2" width="4" height="6" fill="#fff"/></svg>
        +61 3 0462 735 218
      </p>
      <p class="contact__line">
        <svg class="icon" viewBox="0 0 12 12"><rect x="0.5" y="2" width="11" height="8" rx="1" fill="var(--orange)"/><path d="M1 2.5l5 4 5-4" stroke="#fff" stroke-width="1" fill="none"/></svg>
        lionel@brisklesson.com.au
      </p>
    </div>
  </section>

  <section class="card card--back" aria-label="Card back">
    <div class="stripe-panel" role="img" aria-label="Diagonal black and orange stripe pattern"></div>
    <div class="brand-mark">Brisk</div>

    <div class="services">
      <p>Specialising in<br>design and<br>production of<br>training:</p>
      <ul class="services__list">
        <li><svg class="icon" viewBox="0 0 12 12"><rect x="0.5" y="3" width="7.5" height="6" fill="var(--orange)"/><path d="M8 6l3.5-2.5v5z" fill="var(--orange)"/></svg>Video</li>
        <li><svg class="icon" viewBox="0 0 12 12"><circle cx="6" cy="6" r="5" fill="var(--orange)"/></svg>Animation</li>
        <li><svg class="icon" viewBox="0 0 12 12"><path d="M9 1l2 2-6.5 6.5-3 1 1-3z" fill="var(--orange)"/></svg>Illustration</li>
        <li><svg class="icon" viewBox="0 0 12 12"><path d="M2 1H1v10h1M10 1h1v10h-1M3.5 3h5M6 3v6" stroke="var(--orange)" stroke-width="1.2" fill="none"/></svg>Text</li>
      </ul>
      <p class="services__delivery">for delivery via<br>internet, intranet<br>and/or LMS.</p>
    </div>

    <p class="web-address">www.brisklesson.com.au</p>
  </section>
</body>
</html>
```